Consultancy Business Card Design

We need a business card design for a new company based in singapore called FortyOne. FortyOne a boutique consultancy firm offering broad-based business solutions, from conception to re-invention, for ventures from new start-ups to long-running traditional businesses.
Its 2 main divisions (Food & Beverage Operations and Construction & Project Management) have access to a wide range of networks, knowledge bases, and resources to service its clients across numerous diverse sectors. This includes, and is not limited to, construction, F&B, and retail.
We are a company that combines the ambition, boldness and energy of one in the 20s with the dedication, level-headedness and dependability of one entering its 30s. Bridging the experiences of the old with ideals of the young, we draw on the positives of both to create a unique synergy.
We hope to see designs that fits our company profile.
Boutique
FortyOne(Company Name)
Marcus Leow (Name)
Principle Consultant (Title)
F&B and Hospitality (Division)
(+65) 8364 5170 (Contact no.)
marcus@fortyone-example.com.sg (Email)

```html
<!DOCTYPE html>
<html lang="en">
<head>
<meta charset="utf-8">
<title>FortyOne – Business Card</title>
<link rel="stylesheet" href="https://fonts.googleapis.com/css2?family=Lato:wght@400;700&display=swap">
<style>
  :root {
    --backdrop: #dedede;
    --card: #1c1c1c;
    --ink: #ffffff;
    --ink-soft: #e4e4e4;
    --accent: #2a9ad6;
  }
  * { margin: 0; padding: 0; box-sizing: border-box; }
  html, body {
    width: 1200px;
    height: 840px;
    overflow: hidden;
    background: var(--backdrop);
    font-family: "Lato", Arial, sans-serif;
  }
  .canvas { position: relative; width: 1200px; height: 840px; }

  .card {
    position: absolute;
    top: 271px;
    width: 486px;
    height: 281px;
    background: var(--card);
    color: var(--ink);
  }
  .card--front { left: 76px; }
  .card--back { left: 641px; }

  /* Wordmark: plain uppercase, regular weight, open tracking */
  .wordmark {
    display: flex;
    align-items: center;
    gap: 12px;
  }
  .brand-square {
    width: 10px; height: 10px;
    background: var(--accent);
    flex: none;
  }
  .brand-name {
    font-weight: 400;
    text-transform: uppercase;
    line-height: 1;
    color: var(--ink);
    white-space: nowrap;
  }

  /* Front */
  .front-brand {
    position: absolute;
    left: 0; right: 0;
    top: 126px;
    justify-content: center;
  }
  .front-brand .brand-name { font-size: 28px; letter-spacing: 6px; }

  /* Back */
  .back-brand {
    position: absolute;
    left: 26px;
    top: 140px;
  }
  .back-brand .brand-name { font-size: 20px; letter-spacing: 4px; }

  .name-band {
    position: absolute;
    left: 251px;
    right: 0;
    top: 130px;
    height: 42px;
    background: var(--accent);
    text-align: right;
    padding: 4px 24px 0 0;
  }
  .person-name {
    font-weight: 700;
    font-size: 17px;
    line-height: 18px;
    color: var(--ink);
  }
  .person-title {
    font-size: 12.5px;
    line-height: 15px;
    color: var(--ink);
  }
  .division {
    position: absolute;
    left: 25px;
    top: 241px;
    font-size: 13px;
    color: var(--ink-soft);
  }
  .division-highlight { color: var(--accent); }

  .contact-list {
    position: absolute;
    right: 24px;
    top: 224px;
    list-style: none;
    font-size: 13px;
    line-height: 17px;
    color: var(--ink-soft);
    text-align: right;
  }
  .contact-item {
    display: flex;
    align-items: center;
    justify-content: flex-end;
    gap: 6px;
  }
  .contact-icon { width: 12px; height: 12px; display: block; }
</style>
</head>
<body>
<main class="canvas">

  <section class="card card--front" aria-label="Card front">
    <div class="wordmark front-brand">
      <span class="brand-square"></span>
      <span class="brand-name">FortyOne</span>
    </div>
  </section>

  <section class="card card--back" aria-label="Card back">
    <div class="wordmark back-brand">
      <span class="brand-square"></span>
      <span class="brand-name">FortyOne</span>
    </div>

    <div class="name-band">
      <p class="person-name">Marcus Leow</p>
      <p class="person-title">Principle Consultant</p>
    </div>

    <p class="division"><span class="division-highlight">F&amp;B and Hospitality</span> Division</p>

    <ul class="contact-list">
      <li class="contact-item">
        <span>(+65) 8364 5170</span>
        <svg class="contact-icon" viewBox="0 0 12 12" aria-hidden="true">
          <rect x="3" y="2" width="6" height="10" rx="1" fill="var(--accent)"/>
          <rect x="7" y="0" width="1.2" height="3" fill="var(--accent)"/>
          <rect x="4.2" y="3.4" width="3.6" height="3" fill="var(--card)"/>
        </svg>
      </li>
      <li class="contact-item">
        <span>marcus@fortyone-example.com.sg</span>
        <svg class="contact-icon" viewBox="0 0 12 12" aria-hidden="true">
          <rect x="0.5" y="3" width="11" height="7" fill="var(--accent)"/>
          <path d="M0.5 3 L6 7 L11.5 3" fill="none" stroke="var(--card)" stroke-width="0.9"/>
        </svg>
      </li>
    </ul>
  </section>

</main>
</body>
</html>
```